Real Estate Template

I am looking for a template that can be edited in Adobe Photoshop or Adobe Acrobat or Adobe Reader. I am attaching an example. I would like a few different variations. I need a 6.5 x 9 size flyer with the KWRT FLBH Logos on it. Can you please build me a template that is 6.5 X 9 with an editable front and back side of the flyer?

The FLBH logos on the top right of the back of the flyer. (They are attached).
The Provyx, plain badge shape, & Equal Housing Opportunity logos just next to the FLBH logos. (Just to the left of FLBH)

My headshot on the top left of each side with my contact info to look like my business card.

The colors to be the same color scheme as my brand: Sky blue, white, and a gradient silver. (Not the red & gold in my example. Those are old colors).

An editable header & footer on both sides in a silver gradient color.

3 pics on the front and on the back

My company logo on the bottom left of each side.

I can email you the flyer I have now to give you an idea of what I’m trying to create.

My company is Beacon Hollow Estates. The logo is attached, but it is low res. It's probably best if you just type the logo, please. It's as simple as "Beacon" in dark blue and "Hollow Estates" in silver with 70% of an oval around it in sky blue/teel.

Thank you.
Marcus Telling

Business

Sans Serif

```html
<!DOCTYPE html>
<html lang="en">
<head>
<meta charset="utf-8">
<title>Beacon Hollow Estates – Flyer Template</title>
<link rel="stylesheet" href="https://fonts.googleapis.com/css2?family=Open+Sans:wght@400;600;700&display=swap">
<style>
  :root {
    --sky-blue: #0a78c2;
    --navy: #1c3f8f;
    --white: #ffffff;
    --ink: #111111;
    --stage: #eef0f3;
    --silver-dark: #6b6b6b;
    --silver-mid: #a9a9a9;
    --silver-light: #f2f2f2;
    --photo-light: #f4f1ec;
    --photo-warm: #c9b9a3;
    --photo-deep: #6a2a2e;
  }
  * { box-sizing: border-box; margin: 0; padding: 0; }
  html, body {
    width: 1200px; height: 1000px; overflow: hidden;
    background: var(--stage);
    font-family: "Open Sans", Arial, sans-serif;
  }
  .canvas { position: relative; width: 1200px; height: 1000px; }

  .card {
    position: absolute;
    background: var(--white);
    box-shadow: 0 2px 10px rgba(0,0,0,.18);
    overflow: hidden;
  }
  .card--front { left: 25px; top: 20px; width: 940px; height: 665px; z-index: 2; }
  .card--mailer { left: 200px; top: 300px; width: 975px; height: 680px; z-index: 1; }

  .silver-header {
    position: absolute; left: 0; top: 0; right: 0; height: 125px;
    background: linear-gradient(90deg,
      var(--silver-mid) 0%, var(--silver-light) 16%, var(--silver-mid) 34%,
      var(--silver-dark) 52%, var(--silver-mid) 70%, var(--silver-light) 86%, var(--silver-dark) 100%);
  }

  .agent-band { position: absolute; left: 0; right: 0; bottom: 0; height: 205px; }
  .card--mailer .agent-band { height: 270px; }
  .agent-band__fill {
    position: absolute; left: 125px; right: 0; top: 0; bottom: 0;
    background: var(--sky-blue);
  }
  .agent-band__photo {
    position: absolute; left: 0; top: -12px; bottom: 0; width: 152px;
    background: linear-gradient(180deg, var(--photo-light) 0%, var(--photo-warm) 40%, var(--photo-deep) 72%, var(--photo-warm) 100%);
    border-right: 6px solid var(--silver-mid);
    border-radius: 0 70px 0 0 / 0 100% 0 0;
  }
  .card--mailer .agent-band__photo { top: 0; }

  .agent-info { position: absolute; left: 180px; top: 16px; color: var(--white); }
  .brand-mark { display: flex; align-items: center; gap: 8px; margin-bottom: 14px; }
  .brand-mark__dot { width: 14px; height: 14px; border-radius: 50%; background: #5cc8f0; }
  .brand-mark__name { font-weight: 700; font-size: 19px; color: var(--navy); letter-spacing: .5px; }

  .agent-name { font-weight: 700; font-size: 20px; line-height: 1.15; }
  .agent-title { font-size: 15px; line-height: 1.3; }
  .agent-contact { font-size: 12.5px; line-height: 1.45; margin-top: 8px; }
  .badges { display: flex; gap: 6px; margin-top: 4px; }
  .badge { width: 12px; height: 12px; background: var(--white); }
  .badge--wide { width: 26px; }

  .indicia {
    position: absolute; left: 805px; top: 55px; width: 125px; height: 125px;
    border: 1.5px solid var(--ink);
    display: flex; flex-direction: column; justify-content: center; align-items: center;
    font-size: 14px; line-height: 1.25; color: var(--ink); text-align: center;
  }
  .indicia strong { font-weight: 700; }
  .address-box {
    position: absolute; left: 745px; top: 272px; width: 48px; height: 62px;
    border: 1px solid #555;
  }
</style>
</head>
<body>
<div class="canvas">

  <section class="card card--mailer" aria-label="Flyer mailing side">
    <div class="indicia">
      <span>PRSRT STD</span>
      <span>ECRWSS</span>
      <span>U.S.POSTAGE</span>
      <strong>PAID</strong>
      <span>FLBH RETAIL</span>
    </div>
    <div class="address-box"></div>
    <div class="agent-band">
      <div class="agent-band__fill"></div>
      <div class="agent-band__photo" role="img" aria-label="Agent headshot"></div>
      <div class="agent-info">
        <div class="brand-mark">
          <span class="brand-mark__dot"></span>
          <span class="brand-mark__name">Beacon Hollow Estates</span>
        </div>
        <div class="agent-name">Marcus Telling</div>
        <div class="agent-title">PROVYX</div>
        <div class="agent-title">Short Sale Expert</div>
        <div class="agent-contact">
          Cell 555-204-7731<br>
          eFax: 555-318-6642<br>
          Email: HomesWithMarcus@lanternmail.com
        </div>
        <div class="badges"><span class="badge"></span><span class="badge"></span><span class="badge badge--wide"></span></div>
      </div>
    </div>
  </section>

  <section class="card card--front" aria-label="Flyer front side">
    <div class="silver-header"></div>
    <div class="agent-band">
      <div class="agent-band__fill"></div>
      <div class="agent-band__photo" role="img" aria-label="Agent headshot"></div>
      <div class="agent-info">
        <div class="brand-mark">
          <span class="brand-mark__dot"></span>
          <span class="brand-mark__name">Beacon Hollow Estates</span>
        </div>
        <div class="agent-name">Marcus Telling</div>
        <div class="agent-title">PROVYX</div>
        <div class="agent-title">Short Sale Expert</div>
        <div class="agent-contact">
          Cell 555-204-7731<br>
          eFax: 555-318-6642<br>
          Email: HomesWithMarcus@lanternmail.com
        </div>
        <div class="badges"><span class="badge"></span><span class="badge"></span><span class="badge badge--wide"></span></div>
      </div>
    </div>
  </section>

</div>
</body>
</html>
```